Business Card Design Project

I am looking for a minimal matte background/shiny (spot UV) ink monochromatic design with a splash of neon color.

the card should be 2 sided, logo only on one side - all info and possibly logo on the other.

My creative director described the colors he imagined for the design to be:
'it's a dark field, like charcoal or a really dark burgundy, or deep blue, shot through with a neon—but just a tiny bit of it. so a charcoal field with a laser-thin streak of electric lime, safety orange, or cobalt blue. really beautiful stuff.'

here are some samples of the types of cards I am trying to create:
http://www.pictavault.example/photos/dawnpress/6967376935/in/photostream -> Vandrelle Lustre

http://www.pictavault.example/photos/dawnpress/6497659409/in/photostream -> Standard Coated (14pt/matte) with SPOT UV

http://www.pictavault.example/photos/dawnpress/6497658995/in/photostream/ -> Heavy Corvane with Raised Ink

http://www.pictavault.example/photos/dawnpress/6275629165/in/photostream/ -> Standard Coated (14pt/matte) with SPOT UV

Here is my logo:
https://www.filecrate.example/s/sigym192mlh58ge/quillorb%20logotype%20final.ai

Here are the details for info:
Dorian Elwood Marsh
email - dorian@quillorb.example
mobile - 555 013 2867
web -
quillorb.example: inventive technology applications
quillorb-tv.example: innovative video advertising

please let me know if there is anything at all that you need.

Target Market(s)

mid to large agencies that require interactive design and entrepreneurial/startup individuals/companies that need application development.

Industry/Entity Type

Safety

Requirements
Must have
• logo only on one side

```html
<!DOCTYPE html>
<html lang="en">
<head>
<meta charset="utf-8">
<title>Quillorb Business Card</title>
<link href="https://fonts.googleapis.com/css2?family=Oswald:wght@400;500&family=Open+Sans:wght@400;700&display=swap" rel="stylesheet">
<style>
  :root {
    --canvas-bg: #e6e6e4;
    --charcoal: #141414;
    --charcoal-soft: #232323;
    --paper: #ffffff;
    --ink: #2e2e2e;
    --white: #f4f4f4;
    --grey-text: #9a9a9a;
    --tagline-grey: #777777;
    --neon-lime: #c6ff1a;
  }
  * { margin: 0; padding: 0; box-sizing: border-box; }
  html, body {
    width: 1200px; height: 745px; overflow: hidden;
    background: var(--canvas-bg);
  }
  .canvas {
    position: relative; width: 1200px; height: 745px;
    display: flex; align-items: center; justify-content: center; gap: 40px;
  }
  .card {
    position: relative; width: 540px; height: 310px; overflow: hidden;
    box-shadow: 0 6px 18px rgba(0,0,0,0.18);
  }

  /* Info side */
  .card--info { background: var(--charcoal); }
  .hex-field {
    position: absolute; left: 0; top: 40px; width: 300px; height: 270px;
    background: radial-gradient(ellipse at 35% 55%, var(--charcoal-soft) 0%, rgba(35,35,35,0.5) 45%, rgba(20,20,20,0) 75%);
  }
  .brand-small {
    position: absolute; left: 34px; top: 92px;
    display: flex; align-items: center; gap: 8px;
    font-family: "Oswald", sans-serif; font-weight: 400;
    font-size: 15px; letter-spacing: 0.32em; color: var(--white);
  }
  .brand-small .dot {
    width: 7px; height: 7px; border-radius: 50%; background: var(--white);
    margin-top: -14px;
  }
  .neon-streak {
    position: absolute; right: 0; height: 2px;
    background: linear-gradient(to right, rgba(198,255,26,0), var(--neon-lime));
    box-shadow: 0 0 6px rgba(198,255,26,0.55);
  }
  .card--info .neon-streak { top: 78px; width: 250px; }
  .contact {
    position: absolute; left: 300px; top: 92px; width: 230px;
    font-family: "Open Sans", sans-serif; color: var(--grey-text);
  }
  .contact .name {
    font-weight: 700; font-size: 20px; color: var(--white);
    letter-spacing: -0.01em; margin-bottom: 8px; white-space: nowrap;
  }
  .contact p { font-size: 11.5px; line-height: 1.55; white-space: nowrap; }
  .contact .tagline { font-size: 8px; color: var(--tagline-grey); }

  /* Logo side */
  .card--logo { background: var(--paper); }
  .card--logo .neon-streak { top: 150px; width: 96px; }
  .brand-large {
    position: absolute; left: 52px; top: 128px;
    display: flex; align-items: flex-start; gap: 4px;
    font-family: "Oswald", sans-serif; font-weight: 500;
    font-size: 60px; line-height: 1; letter-spacing: 0.3em; color: var(--ink);
  }
  .brand-large .dot {
    width: 14px; height: 14px; border-radius: 50%; background: var(--ink);
    margin-top: -14px;
  }
</style>
</head>
<body>
<main class="canvas">
  <section class="card card--info" aria-label="Card back with contact details">
    <div class="hex-field" role="img" aria-label="Faint dark hexagon pattern"></div>
    <div class="brand-small">QUILLORB<span class="dot"></span></div>
    <div class="neon-streak"></div>
    <div class="contact">
      <p class="name">Dorian Elwood Marsh</p>
      <p>dorian@quillorb.example</p>
      <p>555 013 2867</p>
      <p>quillorb.example <span class="tagline">: inventive technology applications</span></p>
      <p>quillorb-tv.example <span class="tagline">: innovative video advertising</span></p>
    </div>
  </section>
  <section class="card card--logo" aria-label="Card front with logo">
    <div class="brand-large">QUILLORB<span class="dot"></span></div>
    <div class="neon-streak"></div>
  </section>
</main>
</body>
</html>
```